Design to promote Vacation Tune Workshop Series for Kids

We are a small local music school in need of a poster design to promote our new Vacation Tune Workshop Series (sort of like a music camp) for the January 2013 Summer Break here in Sydney, Australia.

We generally teach students private instruments (e.g piano, guitar, bass, singing, drums, trumpet and theory) and offer group classes for Glee Club and Group Guitar.

The proposed Vacation Tune Workshop Series goes for 1 week and is 'Jam Packed' with lots of fun musical activities, workshops and musical experiences.

It's called 'Turn The Tunes Loose' and is designed for Kids aged 7 - 12 yrs of age.

We would like an A3 size poster to be designed and an A6 size flyer which compliments the poster. If you're able to also resize the A3 size poster to A4 that'll be great. The successful candidate can do that once the final design is confirmed.

The look and feel should be 'Summer', fun, musical, hip and targeted at young parents aged 28 - 50yrs old. These parents are generally professionals living in a creative area of Sydney.

Text to be included as follows:

'TURN THE TUNES LOOSE'
A Fun Jam Packed Vacation Tune Workshop Series for the Summer Break

Designed for Kids 7 - 12 years old

14 - 18 January, 2013
NEWTOWN

No experience necessary

INSTRUMENTAL DISCOVERY Learn and play a variety of musical instruments
SONG WRITING Write your own songs
BEAT BOXING Learn to beat box and rap
MUSIC GAMES Join in a number of fun musical games and activities
GLEE Do some singing (no problems if you've never tried)
MUSIC TECHNOLOGY Learn about music technology and how to record/produce songs
HAVE FUN!

EARLY BIRD REGISTRATION: $280 per child (when you enrol by 14 December, 2012)

COST: $300 per child
*discounts apply when enrolling 2 or more kids

Goes from Monday - Friday, 9:00am - 3:00pm

ENROL ONLINE NOW
www.brightkeysounds.com.au
Or call 02 7419 2856 / 0438 967 204

For enquiries or more info visit our website or email info@brightkeysounds.com.au

Bright Key Sound School
Unit 4B, 19 Harlow Street, Newtown (enter via Pembrick Ave)

Target Market(s)

Parents of children aged 7 - 12 yrs. They would be around 25 - 50 yrs old

Industry/Entity Type

School

Requirements
Must have
• Must include our company logo - there are two versions which you can pick from to use.

```html
<!DOCTYPE html>
<html lang="en">
<head>
<meta charset="utf-8">
<title>Turn The Tunes Loose – Vacation Tune Workshop Series</title>
<link href="https://fonts.googleapis.com/css2?family=Luckiest+Guy&family=Pacifico&family=Tinos:ital,wght@0,400;0,700;1,400&display=swap" rel="stylesheet">
<style>
  :root {
    --bg-light: #6b6b6e;
    --bg-dark: #2e2e31;
    --white: #ffffff;
    --cyan: #27b6e6;
    --blue: #1d8fd6;
    --pink: #e8177f;
    --yellow: #f7c21b;
    --orange: #f39a1f;
    --photo-light: #efe4d6;
    --photo-mid: #b8a99b;
  }
  * { margin: 0; padding: 0; box-sizing: border-box; }
  html, body { width: 852px; height: 1200px; overflow: hidden; background: var(--bg-dark); }
  .poster {
    position: relative; width: 852px; height: 1200px; overflow: hidden;
    background: radial-gradient(ellipse at 55% 40%, var(--bg-light) 0%, #49494c 45%, var(--bg-dark) 100%);
    font-family: "Tinos", "Times New Roman", serif; color: var(--white); line-height: 1.2;
  }
  .hero-photo {
    position: absolute; left: 400px; top: 60px; width: 400px; height: 950px;
    background: radial-gradient(ellipse at 50% 62%, var(--photo-light) 0%, var(--photo-mid) 45%, rgba(90,83,82,0) 75%);
  }
  .headline { position: absolute; left: 80px; top: 100px; width: 320px; height: 280px; transform: rotate(-6deg); }
  .headline span { position: absolute; display: block; line-height: 1; }
  .hl-turn { left: 20px; top: 0; font-family: "Luckiest Guy", sans-serif; font-size: 72px; color: var(--cyan);
    text-shadow: 4px 4px 0 var(--pink); }
  .hl-the { left: 10px; top: 80px; padding: 8px 14px 2px; background: var(--yellow); font-family: "Luckiest Guy", sans-serif;
    font-size: 48px; color: var(--pink); }
  .hl-tunes { left: 120px; top: 118px; padding: 0 14px 10px; background: var(--pink); font-family: "Pacifico", cursive;
    font-size: 56px; color: var(--white); }
  .hl-loose { left: 170px; top: 214px; padding: 8px 12px 2px; background: var(--blue); font-family: "Luckiest Guy", sans-serif;
    font-size: 40px; color: var(--white); }
  .details { position: absolute; left: 76px; top: 400px; width: 400px; }
  .tagline { font-style: italic; font-size: 24px; line-height: 1.15; }
  .age { color: var(--orange); font-size: 14px; }
  .dates { margin-top: 14px; color: var(--orange); font-size: 15px; }
  .place { color: var(--orange); font-size: 22px; line-height: 1; }
  .note { font-size: 14px; margin-top: 6px; }
  .program-title { margin-top: 12px; color: var(--cyan); font-size: 18px; }
  .program { list-style: none; font-size: 12px; line-height: 1.3; }
  .program-fun { color: var(--orange); font-size: 22px; margin-top: 4px; }
  .early { margin-top: 20px; font-size: 14px; }
  .price-cyan { margin-top: 4px; color: var(--cyan); font-size: 28px; line-height: 1; white-space: nowrap; }
  .price-pink { margin-top: 10px; color: var(--pink); font-size: 28px; line-height: 1; white-space: nowrap; }
  .small { font-size: 13px; line-height: 1.3; }
  .school-name { margin-top: 22px; color: var(--orange); font-size: 22px; }
  .enrol { position: absolute; left: 380px; top: 994px; font-size: 20px; letter-spacing: 0.5px; }
  .bands { position: absolute; left: 0; top: 1010px; width: 852px; height: 190px; }
  .band-text { position: absolute; color: var(--white); white-space: nowrap; }
  .band-call { left: 76px; top: 1036px; font-size: 18px; transform: rotate(-0.7deg); }
  .band-info { left: 76px; top: 1112px; font-size: 16px; font-style: italic; transform: rotate(-1.8deg); }
  .brand-badge { position: absolute; left: 628px; top: 1002px; width: 156px; height: 156px; border-radius: 50%;
    background: var(--white); display: flex; align-items: center; justify-content: center; text-align: center; }
  .brand-name { color: var(--pink); font-weight: 700; font-size: 19px; line-height: 1.1; width: 110px; }
</style>
</head>
<body>
<main class="poster">
  <div class="hero-photo" role="img" aria-label="Photo of a young girl in a sparkly pink party dress and tiara"></div>

  <h1 class="headline" aria-label="Turn The Tunes Loose">
    <span class="hl-turn">TURN</span>
    <span class="hl-the">THE</span>
    <span class="hl-tunes">Tunes</span>
    <span class="hl-loose">LOOSE</span>
  </h1>

  <section class="details">
    <p class="tagline">A Fun Jam Packed Vacation Tune Workshop Series for the Summer Break</p>
    <p class="age">Designed for Kids 7 - 12 years old</p>
    <p class="dates">14 - 18 January, 2013</p>
    <p class="place">NEWTOWN</p>
    <p class="note">No experience necessary</p>
    <p class="program-title">INSTRUMENTAL DISCOVERY</p>
    <ul class="program">
      <li>Learn and play a variety of musical instruments</li>
      <li>SONG WRITING Write your own songs</li>
      <li>BEAT BOXING Learn to beat box and rap</li>
      <li>MUSIC GAMES Join in a number of fun musical games &amp; activities</li>
      <li>GLEE Do some singing (no problems if you've never tried)</li>
      <li>MUSIC TECHNOLOGY Learn about music technology<br>and how to record/produce songs</li>
    </ul>
    <p class="program-fun">HAVE FUN!</p>
    <p class="early">EARLY BIRD REGISTRATION:</p>
    <p class="price-cyan">$280 PER CHILD</p>
    <p class="small">(when you enrol by 14 December, 2012)</p>
    <p class="price-pink">COST: $300 PER CHILD</p>
    <p class="small">*discounts apply when enrolling 2 or more kids<br>Goes from Monday - Friday, 9:00am - 3:00pm</p>
    <p class="school-name">Bright Key Sound School</p>
    <p class="small">Unit 4B, 19 Harlow Street, Newtown<br>(enter via Pembrick Ave)</p>
  </section>

  <p class="enrol">ENROL ONLINE NOW</p>

  <svg class="bands" viewBox="0 0 852 190" aria-hidden="true">
    <polygon points="0,18 852,8 852,52 0,62" fill="var(--pink)"/>
    <polygon points="0,90 852,66 852,134 0,158" fill="var(--blue)"/>
  </svg>
  <p class="band-text band-call">www.brightkeysounds.com.au Or call 02 7419 2856 / 0438 967 204</p>
  <p class="band-text band-info">For enquiries or more info visit our website or email info@brightkeysounds.com.au</p>

  <div class="brand-badge">
    <span class="brand-name">Bright Key Sound School</span>
  </div>
</main>
</body>
</html>
```